Kenwick Falcons FC Website

We are looking to develop a new website for Kenwick FC. Kenwick FC has now joined with Kenwick Falcons FC and we are looking at a website that can work for both clubs. Kenwick FC play in a local park football competition while kenwick Falcons are a Semi Professional team that plays in the Coastal Premier Division Competition. What we are after is two separate website off the one platform. I have attached both team logos for you to visualise. Also you can look at the existing kenwick website www.kenwickfc-demo.com.au. We are looking for a huge improvement in the website and it will be imperative we have links to sponsors and the sponsors can get regular visuals. Weare looking to move this club forward and have a very professional website that can communicate clearly with the community.

Hi All,

Please remember that the website is to represent two clubs;
1. Kenwick Falcons FC (Competes in Semi Professional League)
2. Kenwick FC (Compete in HBJCA League which is a lower level)

Further to this the Kenwick Falcons FC page will require a player profile page which will show photos of each player and a little bio on each.

Thanks

Reason: Would like to spend more time review existing and new designs

```html
<!DOCTYPE html>
<html lang="en">
<head>
<meta charset="utf-8">
<title>Kenwick FC</title>
<link href="https://fonts.googleapis.com/css2?family=Oswald:wght@400;500&family=Roboto:wght@300;400&display=swap" rel="stylesheet">
<style>
:root{
  --bg:#1f1f1f;--header:#262626;--red:#c4161c;--red-dark:#8e0f13;
  --white:#fff;--grey:#8a8a8a;--light:#e9e9e9;--footer:#1b1b1b;--text:#555;
}
*{margin:0;padding:0;box-sizing:border-box}
html,body{width:847px;height:1200px;overflow:hidden;background:var(--bg);font-family:'Roboto',sans-serif}
.page{position:relative;width:847px;height:1200px}
.abs{position:absolute}
.head-font{font-family:'Oswald',sans-serif}
.header{left:0;top:0;width:847px;height:93px;background:var(--header);border-bottom:1px solid #333}
.brand{left:120px;top:18px;width:70px;height:62px;display:flex;align-items:center;justify-content:center;gap:4px;color:var(--white);font-family:'Oswald',sans-serif;font-size:13px}
.brand i{width:8px;height:8px;background:var(--red);display:block}
.phone{left:535px;top:17px;color:var(--white);font-family:'Oswald',sans-serif;font-size:15px;display:flex;gap:5px;align-items:center}
.phone-note{left:537px;top:34px;color:var(--grey);font-family:'Oswald',sans-serif;font-size:7px;letter-spacing:.2px}
.btn-reg{left:641px;top:16px;width:92px;height:30px;background:var(--red);border:1px solid #e33;color:var(--white);font-family:'Oswald',sans-serif;font-size:10px;display:flex;align-items:center;justify-content:center}
.nav{left:213px;top:67px;display:flex;font-family:'Oswald',sans-serif;font-size:9.5px;color:var(--grey)}
.nav span{position:absolute;white-space:nowrap}
.nav .active{color:var(--white)}
.nav-mark{left:212px;top:89px;width:25px;height:2px;background:var(--red)}
.hero{left:112px;top:93px;width:620px;height:293px;background:linear-gradient(100deg,#5a5a5a 0%,#8c8c8c 40%,#6e6e6e 70%,#3c3c3c 100%)}
.hero-title{left:154px;top:222px;color:#f1f1f1;font-family:'Oswald',sans-serif;font-size:36px;letter-spacing:-1px}
.hero-sub{left:154px;top:273px;color:var(--red);font-size:14px;line-height:19px;font-weight:400}
.arrow{top:217px;width:42px;height:41px;background:#111;display:flex;align-items:center;justify-content:center}
.promo{left:112px;top:386px;width:410px;height:83px;background:linear-gradient(90deg,var(--red-dark),#b31217 60%,#6a0a0d)}
.promo h3{position:absolute;left:20px;top:20px;color:var(--white);font-family:'Oswald',sans-serif;font-size:15px;font-weight:400;letter-spacing:-.5px}
.promo p{position:absolute;left:20px;top:42px;width:370px;color:#f3d6d6;font-size:9.5px;line-height:16px;font-weight:300}
.tile{top:386px;width:105px;height:83px;background:linear-gradient(135deg,#6a6a6a,#bdbdbd)}
.tile span{position:absolute;left:8px;bottom:10px;color:var(--white);font-family:'Oswald',sans-serif;font-size:14px;line-height:19px;letter-spacing:-.6px}
.card{left:113px;width:208px;height:198px;background:var(--white)}
.card .ic{position:absolute;left:0;top:25px;width:27px;height:27px;background:#888;display:flex;align-items:center;justify-content:center}
.card h4{position:absolute;left:43px;top:25px;font-family:'Oswald',sans-serif;font-weight:400;font-size:14px;color:#333}
.card .time{position:absolute;left:43px;top:52px;font-family:'Oswald',sans-serif;font-size:7.5px;color:#999}
.card p{position:absolute;left:43px;top:82px;width:150px;font-size:9px;line-height:16px;color:var(--text);font-weight:300}
.card .more{position:absolute;left:43px;top:163px;font-size:9.5px;color:#d44;font-weight:300}
.card-img{left:321px;width:199px;height:198px}
.hot{left:533px;top:495px;width:198px;height:400px;background:var(--white)}
.hot h3{position:absolute;left:13px;top:14px;font-family:'Oswald',sans-serif;font-weight:400;font-size:14px;color:#333}
.hot .rule{position:absolute;left:0;top:44px;width:198px;height:1px;background:#e2e2e2}
.dots{position:absolute;right:13px;top:20px;display:flex;gap:4px}
.dots i{width:7px;height:7px;border-radius:50%;border:1px solid #aaa;display:block}
.dots i:first-child{background:#aaa}
.item{position:absolute;left:11px;width:180px;height:50px}
.item .thumb{position:absolute;left:0;top:0;width:48px;height:47px}
.item b{position:absolute;left:58px;top:0;font-weight:400;font-size:10px;line-height:13.5px;color:#444;width:125px}
.item small{position:absolute;left:58px;font-size:9px;color:#aaa;font-weight:300}
.hot .all{position:absolute;left:0;width:198px;top:371px;text-align:center;font-size:10px;color:var(--red);text-decoration:underline;font-weight:300}
.sponsors{left:0;top:927px;width:847px;height:84px;background:radial-gradient(ellipse at center,#fafafa,#dcdcdc)}
.sponsor{position:absolute;top:20px;height:44px;display:flex;align-items:center;gap:5px;font-family:'Roboto',sans-serif;font-size:11px;color:#333}
.sponsor i{width:9px;height:9px;background:#999;display:block}
.footer{left:0;top:1011px;width:847px;height:150px;background:var(--footer)}
.col{position:absolute;top:24px;font-size:8px;line-height:15.9px;color:#6d6d6d}
.col .h{font-family:'Oswald',sans-serif;font-size:7.5px;color:#7d7d7d}
.bar{left:0;top:1161px;width:847px;height:39px;background:var(--red);color:var(--white);font-size:8px}
.bar span{position:absolute;top:15px}
</style>
</head>
<body>
<div class="page">
  <header class="abs header">
    <div class="abs brand">Kenwick FC</div>
    <div class="abs phone">
      <svg width="11" height="11" viewBox="0 0 24 24"><path fill="#9a9a9a" d="M6.6 10.8a15 15 0 006.6 6.6l2.2-2.2c.3-.3.7-.4 1-.2 1.1.4 2.3.6 3.6.6.6 0 1 .4 1 1V20c0 .6-.4 1-1 1A17 17 0 013 4c0-.6.4-1 1-1h3.5c.6 0 1 .4 1 1 0 1.3.2 2.5.6 3.6.1.3 0 .7-.2 1z"/></svg>
      0400.123.456
    </div>
    <div class="abs phone-note">ENQUIRIES ONLY AFTER 5PM</div>
    <div class="abs btn-reg">REGISTRATION</div>
    <nav class="abs nav">
      <span class="active" style="left:0">HOME</span>
      <span style="left:62px">LATEST NEWS</span>
      <span style="left:156px">FIXTURE &amp; RESULTS</span>
      <span style="left:272px">PHOTO GALLERY</span>
      <span style="left:374px">SPONSOR CLUB</span>
      <span style="left:474px">CONTACT US</span>
    </nav>
    <div class="abs nav-mark"></div>
  </header>

  <section class="abs hero" role="img" aria-label="Player in club kit running with the ball on a park pitch"></section>
  <div class="abs hero-title">REGISTER NOW</div>
  <div class="abs hero-sub">Lorem ipsum dolor sit amet,<br>consectetur adipisicing elit sed</div>
  <div class="abs arrow" style="left:70px"><svg width="10" height="14"><path d="M8 1L2 7l6 6" stroke="#fff" stroke-width="2" fill="none"/></svg></div>
  <div class="abs arrow" style="left:733px"><svg width="10" height="14"><path d="M2 1l6 6-6 6" stroke="#fff" stroke-width="2" fill="none"/></svg></div>

  <div class="abs promo" role="img" aria-label="Team group photo tinted red">
    <h3>JOIN US. REGISTER NOW.</h3>
    <p>Lorem Ipsum is simply dummy text of the printing and typesetting industry unknown printer took a galley of type and scrambled it ..</p>
  </div>
  <div class="abs tile" style="left:522px" role="img" aria-label="No smoking sign"><span>NO SMOKING<br>BAN</span></div>
  <div class="abs tile" style="left:628px;width:104px" role="img" aria-label="Referee on the pitch"><span>BECOME<br>A REFEREE</span></div>

  <article class="abs card" style="top:494px">
    <div class="ic"><svg width="12" height="10" viewBox="0 0 12 10"><rect x="0" y="2" width="12" height="8" rx="1" fill="#fff"/><rect x="4" y="0" width="4" height="3" fill="#fff"/><circle cx="6" cy="6" r="2" fill="#888"/></svg></div>
    <h4>Banksia Cup Results</h4><div class="time">3 hours ago</div>
    <p>Lorem Ipsum is simply dummy text of the printing and typesetting industry unknown printer took a galley of type and scrambled it ..</p>
    <div class="more">Read more</div>
  </article>
  <div class="abs card-img" style="top:494px;background:linear-gradient(90deg,#b8242a,#7a4b3a 50%,#2b2b33)" role="img" aria-label="Club officials holding a trophy"></div>

  <article class="abs card" style="top:697px">
    <div class="ic"><svg width="12" height="10" viewBox="0 0 12 10"><rect x="0" y="2" width="12" height="8" rx="1" fill="#fff"/><rect x="4" y="0" width="4" height="3" fill="#fff"/><circle cx="6" cy="6" r="2" fill="#888"/></svg></div>
    <h4>Banksia Cup Results</h4><div class="time">3 hours ago</div>
    <p>Lorem Ipsum is simply dummy text of the printing and typesetting industry unknown printer took a galley of type and scrambled it ..</p>
    <div class="more">Read more</div>
  </article>
  <div class="abs card-img" style="top:697px;background:linear-gradient(90deg,#8d8d8d,#b02a2e 55%,#cf1e26)" role="img" aria-label="Commemorative medal beside a red club pennant"></div>

  <aside class="abs hot">
    <h3>WHAT'S HOT</h3>
    <div class="dots"><i></i><i></i><i></i></div>
    <div class="rule"></div>
    <div class="item" style="top:56px"><div class="thumb" style="background:#6b4a30" role="img" aria-label="Finals shield"></div><b>Kenwick FC Finals<br>24th &amp; 25th August</b><small style="top:37px">3 minutes ago</small></div>
    <div class="item" style="top:115px"><div class="thumb" style="background:#b3302c" role="img" aria-label="Team celebrating"></div><b>Kenwick FC Semi-Final results</b><small style="top:37px">7 hours ago</small></div>
    <div class="item" style="top:174px"><div class="thumb" style="background:#a86a66" role="img" aria-label="Junior players"></div><b>Junior Award Day 2013</b><small style="top:23px">23 hours ago</small></div>
    <div class="item" style="top:233px"><div class="thumb" style="background:#6e5546" role="img" aria-label="Young goalkeepers"></div><b>Looking for under 17's Goal keeper</b><small style="top:37px">1 day ago</small></div>
    <div class="item" style="top:292px"><div class="thumb" style="background:#7a6a55" role="img" aria-label="Match action"></div><b>Westbrook Lions<br>Vs Harlow City</b><small style="top:37px">2 days ago</small></div>
    <div class="all">View More News</div>
  </aside>

  <section class="abs sponsors">
    <div class="sponsor" style="left:121px"><i></i>Harbourside Motor Group</div>
    <div class="sponsor" style="left:260px;font-family:'Oswald',sans-serif;font-size:12px">Meridian Bank</div>
    <div class="sponsor" style="left:400px;font-size:13px;color:#b02a2e">Sentrix</div>
    <div class="sponsor" style="left:534px"><i style="background:#7a5a30"></i>Vale Tax</div>
    <div class="sponsor" style="left:617px;font-size:13px">allround media</div>
  </section>

  <footer class="abs footer">
    <div class="col" style="left:118px"><div class="h">HOME</div>News<br>Gallery<br>Sponsor<br>Contact Us</div>
    <div class="col" style="left:172px"><div class="h">CLUB</div>History<br>Committee<br>Awards<br>Forms</div>
    <div class="col" style="left:278px"><div class="h">FIXTURES &amp; RESULTS</div>Premier League<br>Premier League Res<br>Super League<br>Super League Res<br>Under 16 / 2<br>Under 17 / 1</div>
    <div class="col" style="left:370px"><div class="h">&nbsp;</div>Under 10 / 2<br>Under 10 / 3<br>Under 11 / 1<br>Under 12 / 3<br>Under 13 / 3<br>Under 14 / 3</div>
    <div class="col" style="left:475px"><div class="h">&nbsp;</div>AA Men / 5<br>AA Men / 6<br>AA Men / 8<br>AA Men / 10<br>AA Men / 10<br>AA Men / 14</div>
    <div class="col" style="left:580px"><div class="h">&nbsp;</div>07 ECL / Red<br>07 ECL / Green<br>07 ECL / Blue<br>08 ECL / Blue<br>08 ECL / Green<br>09 / Green</div>
    <div class="col" style="left:686px"><div class="h">&nbsp;</div>06 / A Green<br>06 / B Blue<br>06 / C Red<br>06 / D Purple<br>06 / E White<br>06 / F Brown</div>
  </footer>
  <div class="abs bar">
    <span style="left:120px">Copyright © &nbsp;Kenwick FC &nbsp;2014.</span>
    <span style="left:605px">Eastvale Association &nbsp;| &nbsp;Registration</span>
  </div>
</div>
</body>
</html>
```